*** Bakery Needs a Business Card

I need a business card for my new bakery - Pine Lane Baking Dept. We make biscuits, cakes, muffins and other sweets. Our food is honest, wholesome and down to earth - i'd love this to be reflected in the design of the card. The design MUST include our logo (see the attached image - which needs to be replicated). The design should only use 2 or at most 3 colours.

Industry/Entity Type

Bakery

Requirements
Must have
• Must include my logo.
Must have a clean, simple design.
Space for my name, my title, my phone number, my facebook page (I will provide details later)
Should not have
• Must not have lots of bright colours.
Must not have any unnescassry graphics.

```html
<!DOCTYPE html>
<html lang="en">
<head>
<meta charset="utf-8">
<title>Pine Lane Baking Dept. — Business Card</title>
<link rel="stylesheet" href="https://fonts.googleapis.com/css2?family=Cormorant+Garamond:wght@500&family=Open+Sans:wght@600&display=swap">
<style>
  :root {
    --page: #e9e7e4;
    --brown-light: #8a3f24;
    --brown-mid: #6a2814;
    --brown-dark: #3d1207;
    --cream: #f4e6dc;
    --white: #ffffff;
    --panel: rgba(255, 230, 215, 0.08);
    --panel-strong: rgba(255, 220, 200, 0.14);
  }
  * { margin: 0; padding: 0; box-sizing: border-box; }
  html, body {
    width: 1067px;
    height: 1200px;
    overflow: hidden;
    background: var(--page);
  }
  .business-card {
    position: absolute;
    left: 53px;
    top: 325px;
    width: 960px;
    height: 549px;
    overflow: hidden;
    box-shadow: 0 6px 24px rgba(0, 0, 0, 0.25);
  }
  .card-texture {
    position: absolute;
    inset: 0;
    background:
      radial-gradient(ellipse 70% 60% at 55% 40%, var(--brown-light) 0%, var(--brown-mid) 55%, var(--brown-dark) 100%);
  }
  .brand-name {
    position: absolute;
    left: 184px;
    top: 66px;
    font-family: "Open Sans", sans-serif;
    font-weight: 600;
    font-size: 82px;
    line-height: 1;
    letter-spacing: -1px;
    color: var(--white);
    white-space: nowrap;
  }
  .contact-block {
    position: absolute;
    left: 391px;
    top: 252px;
    width: 535px;
    font-family: "Cormorant Garamond", serif;
    font-weight: 500;
    text-align: right;
  }
  .identity-row {
    background: var(--panel-strong);
    padding: 12px 14px 10px;
    color: var(--cream);
  }
  .person-name {
    font-size: 29px;
    line-height: 1.05;
    text-transform: uppercase;
    letter-spacing: 0.5px;
  }
  .person-title {
    font-size: 26px;
    line-height: 1.1;
  }
  .phone-row {
    margin-top: 14px;
    background: var(--white);
    color: var(--brown-mid);
    font-size: 30px;
    line-height: 50px;
    padding: 0 14px;
  }
  .social-row {
    margin-top: 14px;
    background: var(--panel);
    color: var(--cream);
    font-size: 30px;
    line-height: 54px;
    padding: 0 14px;
    letter-spacing: 0.5px;
    white-space: nowrap;
  }
</style>
</head>
<body>
  <section class="business-card">
    <div class="card-texture" role="img" aria-label="Faint damask pattern on warm brown card background"></div>
    <div class="brand-name">PINE LANE</div>
    <div class="contact-block">
      <div class="identity-row">
        <p class="person-name">Daniel Hayes</p>
        <p class="person-title">Title</p>
      </div>
      <p class="phone-row">000.555.0182</p>
      <p class="social-row">pinelanebaking.example</p>
    </div>
  </section>
</body>
</html>
```